Municipal election sign

I am looking to have a sign and a post card designed for an upcoming election in the MD of Larkhaven Alberta Canada. Having my name (Joel Branwick) on the sign/Post card in big clear letters is important as well as the election date(October 16th) The position, if it matters is counselor in Ward 6. On the post cards I would like have some of my key points from the about section of my fb page(Link bellow) on the back of the card.

https://www.pagelink.example/Joelbranwickward6

```html
<!DOCTYPE html>
<html lang="en">
<head>
<meta charset="utf-8">
<title>Joel Branwick – Postcard Options</title>
<link href="https://fonts.googleapis.com/css2?family=Montserrat:wght@400;500;700;800;900&display=swap" rel="stylesheet">
<style>
:root{
  --canvas:#48484a;
  --red:#c8213a;
  --ink:#1d1d1f;
  --grey:#9a9a9c;
  --grey-light:#c9c9cb;
  --cream:#f3f1ea;
  --blue:#3f3f9a;
  --blue-deep:#2e2e80;
  --text:#555;
}
*{margin:0;padding:0;box-sizing:border-box}
html,body{width:1200px;height:800px;overflow:hidden}
body{background:var(--canvas);font-family:"Montserrat",sans-serif;position:relative}
.option-label{position:absolute;color:#fff;font-weight:700;font-size:14px;letter-spacing:.02em}
.card{position:absolute;width:250px;height:180px;overflow:hidden;box-shadow:0 3px 10px rgba(0,0,0,.35)}
.photo{position:absolute;left:0;bottom:0;width:92px;height:180px;
  background:linear-gradient(180deg,#d9b39c 0%,#8a6f63 38%,#5b6fb4 60%,#3e4f8e 100%)}
.flag{position:absolute;background:linear-gradient(90deg,var(--red) 0 28%,#fff 28% 72%,var(--red) 72%)}
.name{position:absolute;color:var(--ink);line-height:.9;text-align:center}
.name .first{display:block;font-weight:900;font-size:50px;letter-spacing:-.02em}
.name .last{display:block;font-weight:800;font-size:21px;letter-spacing:-.01em}
.date{position:absolute;font-size:14px;font-weight:400}
.ward{position:absolute;font-size:8.5px;font-weight:400;white-space:nowrap}
.ward b{font-weight:800;font-size:10px}
.back{background:var(--cream)}
.back-heading{position:absolute;left:8px;top:14px;width:190px;padding:3px 6px;color:#fff;
  font-weight:700;font-size:8px;line-height:1.05;background:var(--grey)}
.stamp{position:absolute;right:10px;top:12px;width:28px;height:30px;border:1px dashed #aaa}
.points{position:absolute;left:14px;top:48px;width:222px;font-size:4.8px;line-height:1.25;color:var(--text)}
.points dt{color:var(--red);font-weight:500;margin-top:4px}
.points dt:first-child{margin-top:0}
.points dd{margin:0}
.wave{position:absolute;left:0;top:0;width:250px;height:180px}
.o1-front{background:radial-gradient(circle at 65% 35%,#fff 0%,#e6e6e6 80%)}
.o1-back{background:radial-gradient(circle at 60% 60%,#fff 0%,#e8e8e8 90%)}
.o1-back .back-heading{left:0;top:10px;width:250px;padding:4px 8px;background:var(--red)}
.o1-back .points dt{font-weight:700}
.o1-back .rule{position:absolute;left:8px;right:8px;bottom:12px;height:1px;background:#bbb}
.o2-front{background:linear-gradient(135deg,var(--blue) 0%,var(--blue-deep) 100%)}
</style>
</head>
<body>

<div class="option-label" style="left:44px;top:33px">OPTION_1</div>
<div class="card o1-front" style="left:45px;top:118px">
  <svg class="wave" viewBox="0 0 250 180" aria-hidden="true"><path d="M0 110 L250 92 L250 180 L0 180Z" fill="var(--red)"/></svg>
  <div class="photo" role="img" aria-label="Portrait photo of the candidate smiling, arms crossed, in a blue shirt"></div>
  <div class="name" style="left:96px;top:24px;width:150px"><span class="first">JOEL</span><span class="last">BRANWICK</span></div>
  <div class="date" style="right:10px;top:110px;color:#fff">October 16th</div>
  <div class="ward" style="right:10px;bottom:12px;color:#fff"><b>MD</b> of Larkhaven Ward 6</div>
</div>
<div class="card back o1-back" style="left:311px;top:118px">
  <div class="back-heading">A FEW POINTS THAT I FEEL ARE<br>IMPORTANT IN THE MD</div>
  <div class="stamp" style="top:16px;border-color:#ccc"></div>
  <dl class="points" style="top:46px;width:200px">
    <dt>Taking advantage of Federal and provincial grant money:</dt>
    <dd>I work for Norvale Networks, a local internet service provider and have seen multiple opportunities for us as a region (City of Ashmere, MD of Larkhaven, Town of Larkhaven and Ashmere First Nation) to take advantage of grant money. Unfortunately, these applications never came to fruition. I feel that we need to take advantages of all opportunities as a region, and work together to better the Northshore area.</dd>
    <dt>Growth in the MD:</dt>
    <dd>In a time of recession we need to make sure the MD of Larkhaven remains a competitive place to do business and to live, this means looking at the taxes for both business and residential.</dd>
    <dt>Strengthen relationships with adjacent Municipalities:</dt>
    <dd>Working with other municipalities to better our region.</dd>
  </dl>
  <div class="rule"></div>
</div>

<div class="option-label" style="right:44px;top:33px">OPTION_2</div>
<div class="card o2-front" style="left:631px;top:118px">
  <div class="flag" role="img" aria-label="Waving Canadian flag" style="left:60px;top:-10px;width:120px;height:62px;transform:skewY(-8deg)"></div>
  <div class="photo" role="img" aria-label="Portrait photo of the candidate smiling, arms crossed, in a blue shirt"></div>
  <div class="name" style="left:104px;top:64px;width:142px;color:#fff"><span class="first" style="font-size:44px">JOEL</span><span class="last" style="font-size:19px">BRANWICK</span></div>
  <div class="date" style="left:104px;top:121px;width:142px;text-align:center;color:#fff">October 16th</div>
  <div class="ward" style="left:92px;right:0;top:150px;height:14px;line-height:14px;text-align:center;background:#fff;color:var(--blue-deep)"><b>MD</b> of Larkhaven Ward 6</div>
</div>
<div class="card back" style="left:897px;top:118px">
  <svg class="wave" viewBox="0 0 250 180" aria-hidden="true"><path d="M0 150 C80 118 160 168 250 118 L250 132 C160 182 80 138 0 166Z" fill="var(--grey-light)"/><path d="M70 180 C150 172 205 152 250 128 L250 180Z" fill="var(--red)"/></svg>
  <div class="back-heading">A FEW POINTS THAT I FEEL ARE<br>IMPORTANT IN THE MD</div>
  <div class="stamp"></div>
  <dl class="points">
    <dt>Strengthen relationships with adjacent Municipalities:</dt><dd>Working with other municipalities to better our region.</dd>
    <dt>Recreation and community hall funding:</dt><dd>We should look at building more parks, ice rinks and walking trails throughout the MD.</dd>
    <dt>Help bring doctors to the City of Ashmere:</dt><dd>Currently most residents from Ward 6 go to Ashmere for medical services. The MD of Larkhaven should work with the City as much as possible to help our residents get easier access to medical services.</dd>
  </dl>
</div>

<div class="option-label" style="left:44px;top:409px">OPTION_3</div>
<div class="card" style="left:45px;top:494px;background:radial-gradient(circle at 60% 40%,#fff 0%,#e4e4e4 85%)">
  <div class="flag" role="img" aria-label="Waving Canadian flag" style="left:50px;top:-10px;width:120px;height:68px;transform:skewY(-6deg)"></div>
  <div class="photo" role="img" aria-label="Portrait photo of the candidate smiling, arms crossed, in a blue shirt"></div>
  <div class="name" style="left:104px;top:66px;width:142px"><span class="first" style="font-size:44px">JOEL</span><span class="last" style="font-size:19px">BRANWICK</span></div>
  <div class="date" style="left:104px;top:122px;width:142px;text-align:right;padding-right:8px;color:var(--ink)">October 16th</div>
  <div class="ward" style="left:100px;right:0;top:146px;height:16px;line-height:16px;text-align:center;background:var(--grey);color:#fff"><b>MD</b> of Larkhaven Ward 6</div>
</div>
<div class="card back" style="left:311px;top:494px">
  <svg class="wave" viewBox="0 0 250 180" aria-hidden="true"><path d="M0 150 C80 118 160 168 250 118 L250 132 C160 182 80 138 0 166Z" fill="var(--grey-light)"/><path d="M70 180 C150 172 205 152 250 128 L250 180Z" fill="var(--red)"/></svg>
  <div class="back-heading">A FEW POINTS THAT I FEEL ARE<br>IMPORTANT IN THE MD</div>
  <div class="stamp"></div>
  <dl class="points">
    <dt>Strengthen relationships with adjacent Municipalities:</dt><dd>Working with other municipalities to better our region.</dd>
    <dt>Recreation and community hall funding:</dt><dd>We should look at building more parks, ice rinks and walking trails throughout the MD.</dd>
    <dt>Help bring doctors to the City of Ashmere:</dt><dd>Currently most residents from Ward 6 go to Ashmere for medical services. The MD of Larkhaven should work with the City as much as possible to help our residents get easier access to medical services.</dd>
  </dl>
</div>

<div class="option-label" style="right:44px;top:409px">OPTION_4</div>
<div class="card" style="left:631px;top:494px;background:var(--cream)">
  <svg class="wave" viewBox="0 0 250 180" aria-hidden="true"><path d="M0 40 C40 10 90 30 140 18 L140 34 C95 48 45 30 0 70Z" fill="var(--red)"/><path d="M0 110 C20 95 40 100 60 96 L60 120 C40 122 20 118 0 130Z" fill="var(--red)"/></svg>
  <div class="photo" role="img" aria-label="Portrait photo of the candidate smiling, arms crossed, in a blue shirt" style="left:6px;width:92px"></div>
  <div style="position:absolute;right:10px;top:8px;text-align:right;line-height:1">
    <div style="font-weight:800;font-size:12px;color:var(--grey)">MD</div>
    <div style="font-size:8.5px;color:var(--ink)">of Larkhaven Ward 6</div>
  </div>
  <div class="name" style="left:104px;top:80px;width:142px"><span class="first" style="font-size:42px">JOEL</span><span class="last" style="font-size:19px">BRANWICK</span></div>
  <div class="date" style="left:104px;right:0;top:146px;height:18px;line-height:18px;text-align:center;background:var(--grey);color:#fff">October 16th</div>
</div>
<div class="card back" style="left:897px;top:494px">
  <svg class="wave" viewBox="0 0 250 180" aria-hidden="true"><path d="M0 150 C80 118 160 168 250 118 L250 132 C160 182 80 138 0 166Z" fill="var(--grey-light)"/><path d="M70 180 C150 172 205 152 250 128 L250 180Z" fill="var(--red)"/></svg>
  <div class="back-heading">A FEW POINTS THAT I FEEL ARE<br>IMPORTANT IN THE MD</div>
  <div class="stamp"></div>
  <dl class="points">
    <dt>Strengthen relationships with adjacent Municipalities:</dt><dd>Working with other municipalities to better our region.</dd>
    <dt>Recreation and community hall funding:</dt><dd>We should look at building more parks, ice rinks and walking trails throughout the MD.</dd>
    <dt>Help bring doctors to the City of Ashmere:</dt><dd>Currently most residents from Ward 6 go to Ashmere for medical services. The MD of Larkhaven should work with the City as much as possible to help our residents get easier access to medical services.</dd>
  </dl>
</div>

</body>
</html>
```